依頼概要
■依頼の目的、概要
当店では補聴器、周辺機器の取扱いをしています。
(株)ベルカナのケルヴァネスト®の取扱いを開始しました。
主に老人、介護施設向けのダイレクトメールの作成をお願いします。

■依頼内容
デザイン案 (株)ベルカナホームページを参考に作成してください。
ハガキサイズ 表裏両面を作成してください。
ケルヴァネスト®ポルテを主に取り扱います。
詳細は添付ファイルをご確認ください。

1週間無料試聴可能です。と記載して下さい。

スッキリとして見やすく、ケルヴァネスト®のイメージに一番合っていると思いましたので、選ばせて頂きました。料金別納マークもデザインして頂いたこともポイントです。素敵なデザインをありがとうございました。

皆様、力作ぞろいで選ぶことが大変でした。同じ製品でも、提案する人によりデザインやアプローチが大きく異なったことが印象的でした。これからも、チラシやロゴ等をお願いする事もありますので、素敵なデザインをお願い致します。ありがとうございました。

```html
<!DOCTYPE html>
<html lang="ja">
<head>
<meta charset="utf-8">
<title>ミミサポート清水丘 ダイレクトメール 宛名面</title>
<link rel="stylesheet" href="https://fonts.googleapis.com/css2?family=Noto+Sans+JP:wght@400;500;700;900&family=Noto+Serif+JP:wght@400;700;900&display=swap">
<style>
  :root {
    --paper: #ffffff;
    --ink: #1a1a1a;
    --purple: #7a5a9a;
    --cyan: #17a8e0;
    --badge: #f3d21c;
    --frame: #9a9a9a;
    --photo-light: #eef0f2;
    --photo-dark: #c9ccd1;
  }
  html, body {
    margin: 0;
    padding: 0;
    overflow: hidden;
    background: var(--paper);
  }
  .postcard {
    position: relative;
    width: 809px;
    height: 1200px;
    box-sizing: border-box;
    border: 2px solid var(--frame);
    background: var(--paper);
    font-family: "Noto Sans JP", sans-serif;
    color: var(--ink);
    overflow: hidden;
  }
  .postcard-title {
    position: absolute;
    top: 30px;
    left: 0;
    width: 100%;
    text-align: center;
    font-family: "Noto Serif JP", serif;
    font-size: 22px;
    letter-spacing: 6px;
    color: var(--purple);
  }
  .postage-mark {
    position: absolute;
    left: 59px;
    top: 116px;
    width: 162px;
    height: 208px;
    box-sizing: border-box;
    border: 2px solid var(--ink);
  }
  .postage-mark__label {
    height: 38px;
    border-bottom: 2px solid var(--ink);
    text-align: center;
    line-height: 38px;
    font-size: 20px;
    font-weight: 500;
    letter-spacing: 1px;
  }
  .postage-mark__symbol {
    display: block;
    margin: 40px auto 0;
  }
  .product-photo {
    position: absolute;
    left: 135px;
    top: 764px;
    width: 210px;
    height: 240px;
    background: linear-gradient(135deg, var(--photo-light), var(--photo-dark));
  }
  .new-badge {
    position: absolute;
    left: 22px;
    top: 768px;
    width: 104px;
    height: 56px;
    border-radius: 28px;
    background: var(--badge);
    color: var(--paper);
    font-weight: 900;
    font-size: 28px;
    font-style: normal;
    text-align: center;
    line-height: 56px;
    letter-spacing: 1px;
  }
  .product-name {
    position: absolute;
    left: 22px;
    top: 1070px;
    width: 190px;
  }
  .product-name__en {
    font-weight: 900;
    font-size: 30px;
    line-height: 1;
    letter-spacing: 1px;
  }
  .product-name__ja {
    margin-top: 8px;
    font-size: 15px;
    font-weight: 500;
  }
  .trial-box {
    position: absolute;
    left: 224px;
    top: 1042px;
    width: 120px;
    height: 146px;
    background: var(--cyan);
    color: var(--paper);
    text-align: center;
    display: flex;
    flex-direction: column;
    justify-content: center;
    gap: 4px;
  }
  .trial-box__period { font-size: 22px; font-weight: 500; }
  .trial-box__free { font-size: 40px; font-weight: 700; line-height: 1.1; }
  .trial-box__note { font-size: 20px; font-weight: 500; }
  .shop-info {
    position: absolute;
    left: 380px;
    top: 770px;
    width: 400px;
    text-align: center;
  }
  .shop-info__mark { display: block; margin: 0 auto 8px; }
  .shop-info__category {
    font-family: "Noto Serif JP", serif;
    font-weight: 700;
    font-size: 22px;
    letter-spacing: 2px;
  }
  .shop-info__name {
    font-family: "Noto Serif JP", serif;
    font-weight: 900;
    font-size: 38px;
    letter-spacing: 2px;
    margin-top: 2px;
  }
  .shop-info__contact {
    text-align: left;
    margin: 6px 0 0 18px;
  }
  .shop-info__address { font-size: 20px; }
  .shop-info__line {
    font-size: 32px;
    font-weight: 500;
    line-height: 1.25;
  }
  .shop-info__line--mail { font-size: 26px; }
  .shop-info__tag {
    color: var(--purple);
    font-size: 20px;
    font-weight: 500;
    margin-right: 6px;
  }
  .shop-info__web {
    margin-top: 10px;
    font-family: "Noto Serif JP", serif;
    font-weight: 700;
    font-size: 27px;
    letter-spacing: 2px;
    color: var(--purple);
  }
</style>
</head>
<body>
  <main class="postcard">
    <div class="postcard-title">郵便はがき</div>

    <div class="postage-mark">
      <div class="postage-mark__label">料金別納郵便</div>
      <svg class="postage-mark__symbol" width="70" height="70" viewBox="0 0 70 70" aria-hidden="true">
        <circle cx="35" cy="35" r="30" fill="none" stroke="var(--purple)" stroke-width="4"/>
      </svg>
    </div>

    <div class="product-photo" role="img" aria-label="ケルヴァネスト®ポルテ スピーカー2台の製品写真"></div>
    <div class="new-badge">NEW</div>

    <div class="product-name">
      <div class="product-name__en">KELVANEST</div>
      <div class="product-name__ja">【ケルヴァネスト®】</div>
    </div>

    <div class="trial-box">
      <div class="trial-box__period">1週間</div>
      <div class="trial-box__free">無料</div>
      <div class="trial-box__note">試聴可能</div>
    </div>

    <section class="shop-info">
      <svg class="shop-info__mark" width="76" height="76" viewBox="0 0 76 76" aria-hidden="true">
        <circle cx="38" cy="38" r="33" fill="none" stroke="var(--purple)" stroke-width="4"/>
      </svg>
      <div class="shop-info__category">補聴器専門店</div>
      <div class="shop-info__name">ミミサポート清水丘</div>
      <div class="shop-info__contact">
        <div class="shop-info__address">〒420-0000 静岡市葵区3番町5-2</div>
        <div class="shop-info__line"><span class="shop-info__tag">Tel･Fax</span>054-000-1234</div>
        <div class="shop-info__line shop-info__line--mail"><span class="shop-info__tag">Mail</span>mimi-sup@example.jp</div>
      </div>
      <div class="shop-info__web">www.mimi-sup.example</div>
    </section>
  </main>
</body>
</html>
```